ko7ara card

the business is a virtual space for showcasing art, libraries, science, food and gifts

high end - new look - nothing fussy - clean lines - bit of colour

needs to last for ten years - at least

think the number 11 in yellow with a purple background

hope that is enough of a brief - smile

Target Market(s)

all ages

Industry/Entity Type

Business

Contact Information for Business Card

ko7ara.com
tam corley = caretaker
virtual space & ashbrook bay > westcoast

Requirements
Must have
• happy for you to choose
Nice to have
• ditto
Should not have
• anything boring - something that appeals to Gen I

```html
<!DOCTYPE html>
<html lang="en">
<head>
<meta charset="utf-8">
<title>ko7ara card</title>
<link rel="stylesheet" href="https://fonts.googleapis.com/css2?family=Bitter:wght@700;800&display=swap">
<style>
  :root {
    --backdrop: #e8e5e0;
    --white: #ffffff;
    --yellow: #ffe600;
    --ink: #111111;
    --paint-purple: #5b3a9e;
    --paint-blue: #1f8fd6;
    --paint-navy: #1b2a6b;
    --paint-green: #2f9a4a;
    --paint-yellow: #f4d21c;
    --paint-red: #d9271e;
    --paint-orange: #f08a1c;
    --paint-sky: #2fb0ee;
    --card-shadow: 0 18px 40px rgba(0,0,0,0.22);
  }
  * { box-sizing: border-box; margin: 0; padding: 0; }
  html, body {
    width: 1200px;
    height: 784px;
    overflow: hidden;
    background: var(--backdrop);
  }
  .canvas {
    width: 1200px;
    height: 784px;
    display: flex;
    align-items: center;
    justify-content: center;
    gap: 60px;
  }
  .card {
    position: relative;
    width: 520px;
    height: 310px;
    border-radius: 4px;
    overflow: hidden;
    box-shadow: var(--card-shadow);
    font-family: "Bitter", Georgia, serif;
  }
  .card__artwork {
    position: absolute;
    inset: 0;
  }
  .card--front .card__artwork {
    background:
      radial-gradient(circle at 68% 42%, var(--paint-yellow) 0%, transparent 22%),
      radial-gradient(circle at 30% 70%, var(--paint-green) 0%, transparent 30%),
      radial-gradient(circle at 85% 80%, var(--paint-blue) 0%, transparent 30%),
      linear-gradient(135deg, var(--paint-navy) 0%, var(--paint-purple) 45%, var(--paint-blue) 100%);
  }
  .card--back .card__artwork {
    background:
      radial-gradient(ellipse at 45% 55%, var(--white) 0%, transparent 20%),
      radial-gradient(ellipse at 20% 75%, var(--paint-yellow) 0%, transparent 30%),
      radial-gradient(ellipse at 80% 85%, var(--paint-red) 0%, transparent 30%),
      radial-gradient(ellipse at 15% 20%, var(--paint-orange) 0%, transparent 25%),
      linear-gradient(160deg, var(--paint-sky) 0%, var(--paint-blue) 50%, var(--paint-red) 100%);
  }
  .wordmark {
    position: absolute;
    color: var(--white);
    font-weight: 800;
    letter-spacing: 1px;
    line-height: 1;
  }
  .card--front .wordmark {
    left: 34px;
    bottom: 34px;
    font-size: 96px;
  }
  .card--back .wordmark {
    top: 24px;
    right: 30px;
    font-size: 64px;
  }
  .contact {
    position: absolute;
    left: 34px;
    bottom: 26px;
    width: 300px;
    color: var(--white);
    text-shadow:
      -1px -1px 0 var(--ink), 1px -1px 0 var(--ink),
      -1px 1px 0 var(--ink), 1px 1px 0 var(--ink),
      0 2px 4px rgba(0,0,0,0.6);
    line-height: 1.15;
  }
  .contact__name {
    color: var(--yellow);
    font-size: 22px;
    font-weight: 800;
  }
  .contact__role {
    font-size: 14px;
    font-weight: 700;
    margin-bottom: 6px;
  }
  .contact__phone,
  .contact__web {
    color: var(--yellow);
    font-size: 25px;
    font-weight: 800;
  }
  .contact__address {
    margin-top: 4px;
    font-size: 17px;
    font-weight: 700;
  }
</style>
</head>
<body>
  <main class="canvas">
    <section class="card card--front">
      <div class="card__artwork" role="img" aria-label="Abstract expressionist painting in deep blue, purple, yellow and green brushwork"></div>
      <div class="wordmark">ko7ara</div>
    </section>

    <section class="card card--back">
      <div class="card__artwork" role="img" aria-label="Abstract palette-knife painting in bright blue, yellow, white and red strokes"></div>
      <div class="wordmark">ko7ara</div>
      <div class="contact">
        <p class="contact__name">Tam Corley</p>
        <p class="contact__role">steward of the openroom<br>&amp; ashbrook bay &gt; westcoast</p>
        <p class="contact__phone">618 - 402 - 315 - 977</p>
        <p class="contact__web">ko7ara.com</p>
        <p class="contact__address">14 Marlow Lane Leederville<br>WA 6007</p>
      </div>
    </section>
  </main>
</body>
</html>
```